" Iniciamos o projeto do cliente com análise do consumo de energia elétrica, a partir disso dimensionamos o sistema utilizando a melhor solução de energia solar fotovoltaica para o cliente. Elaboramos a proposta do projeto com o orçamento e após aceite do cliente iniciamos o processo de homologação junto às concessionárias e instalação do sistema no cliente com a nossa própria equipe técnica. Também apresentamos o saving e payback do projeto. "

```html
<!DOCTYPE html>
<html lang="pt-BR">
<head>
<meta charset="UTF-8">
<title>Como Funciona – Raiomar</title>
<link href="https://fonts.googleapis.com/css2?family=Montserrat:wght@400;600;700;800;900&family=Open+Sans:wght@400;600&display=swap" rel="stylesheet">
<style>
  :root{
    --navy:#1b2f5c;
    --navy-deep:#14264d;
    --orange:#ef7d1a;
    --orange-light:#f6a34b;
    --text:#6d6f73;
    --page:#ececec;
    --white:#ffffff;
    --sky:#5f8fd0;
    --panel:#2c4f8f;
  }
  *{box-sizing:border-box;margin:0;padding:0}
  html,body{width:1200px;height:1200px;overflow:hidden;background:var(--page)}
  body{position:relative;font-family:"Open Sans",Arial,sans-serif}
  .slide{position:absolute;left:20px;top:274px;width:1160px;height:652px;background:var(--white);overflow:hidden;box-shadow:0 2px 10px rgba(0,0,0,.12)}
  .header-photo{position:absolute;right:0;top:0;width:500px;height:92px;background:linear-gradient(115deg,var(--sky) 0%,var(--panel) 45%,#1d3a72 70%,#f0b35a 100%);clip-path:polygon(14% 0,100% 0,100% 100%,0 100%)}
  .brand{position:absolute;right:52px;top:22px;width:200px;height:52px;background:var(--white);display:flex;align-items:center;justify-content:center;gap:10px}
  .brand-dot{width:18px;height:18px;border-radius:50%;background:var(--navy)}
  .brand-name{font-family:"Montserrat",sans-serif;font-weight:700;font-size:24px;color:var(--navy)}
  .header-rule{position:absolute;left:0;right:0;top:92px;height:3px;background:var(--navy)}
  .title{position:absolute;left:108px;top:160px;font-family:"Montserrat",sans-serif;font-weight:900;font-size:40px;letter-spacing:-.5px;line-height:1}
  .title .accent{color:var(--orange)}
  .title .main{color:var(--navy)}
  .title-bar{position:absolute;left:0;top:214px;width:400px;height:6px;background:var(--navy)}
  .title-bar::after{content:"";position:absolute;right:0;top:6px;width:160px;height:3px;background:var(--orange)}
  .steps{position:absolute;left:36px;top:292px;width:560px;list-style:none}
  .step{position:relative;padding-left:38px;margin-bottom:14px}
  .step-num{position:absolute;left:0;top:0;width:30px;height:30px;border-radius:50%;background:var(--orange);color:var(--white);font-family:"Montserrat",sans-serif;font-weight:800;font-size:18px;display:flex;align-items:center;justify-content:center;box-shadow:inset 0 0 0 3px var(--orange-light)}
  .step-title{font-family:"Montserrat",sans-serif;font-weight:700;font-size:13.5px;color:var(--navy);line-height:1.2}
  .step-text{font-size:10.2px;line-height:1.38;color:var(--text);margin-top:2px}
  .illustration{position:absolute;left:610px;top:232px;width:530px;height:350px;background:linear-gradient(180deg,#ffffff 0%,#eef2f7 35%,#d9dde3 60%,#63b04a 82%,#3f8f2e 100%);border-radius:6px}
  .footer-line{position:absolute;left:0;right:0;bottom:32px;height:3px;background:var(--sky)}
  .footer-band{position:absolute;left:0;right:0;bottom:0;height:32px;background:var(--navy-deep)}
</style>
</head>
<body>
  <section class="slide">
    <div class="header-photo" role="img" aria-label="Foto de painéis solares sob o céu azul"></div>
    <div class="brand"><span class="brand-dot"></span><span class="brand-name">Raiomar</span></div>
    <div class="header-rule"></div>

    <h1 class="title"><span class="accent">COMO</span> <span class="main">FUNCIONA?</span></h1>
    <div class="title-bar"></div>

    <ol class="steps">
      <li class="step">
        <span class="step-num">1</span>
        <h2 class="step-title">O Painel Solar gera a energia solar fotovoltaica</h2>
        <p class="step-text">O Painel Solar reage com a luz do sol e produz energia elétrica (energia fotovoltaica). Os painéis solares, instalados sobre o seu telhado, são conectados um aos outros e então conectados no seu Inversor Solar.</p>
      </li>
      <li class="step">
        <span class="step-num">2</span>
        <h2 class="step-title">O Inversor Solar converte a energia solar para a sua casa ou empresa</h2>
        <p class="step-text">Um Inversor Solar converte a energia solar dos seus painéis fotovoltaicos (Corrente Contínua - CC) em energia elétrica que pode ser usada em sua Casa ou Empresa para a TV, Computador, Máquinas, Equipamentos, e qualquer equipamento elétrico (Corrente Alternada - AC) que você precise usar.</p>
      </li>
      <li class="step">
        <span class="step-num">3</span>
        <h2 class="step-title">A Energia Solar é distribuída para sua casa ou empresa</h2>
        <p class="step-text">A energia que sai do inversor solar vai para o seu “quadro de luz” e é distribuída para sua casa ou empresa, e assim reduz a quantidade de energia que você compra da distribuidora.</p>
      </li>
      <li class="step">
        <span class="step-num">4</span>
        <h2 class="step-title">O excesso de energia vai para a rede da distribuidora gerando créditos!</h2>
        <p class="step-text">O excesso de eletricidade volta para a rede elétrica através do relógio de luz (medidor de energia bi-direcional). Esse medidor registra a energia da sua que é consumida quando não tem sol e, a energia solar gerada em excesso quando tem muito sol e é injetada na rede da distribuidora. A energia solar que vai para a rede vira “crédito de energia” para serem utilizado de noite ou nos próximos meses.</p>
      </li>
    </ol>

    <div class="illustration" role="img" aria-label="Ilustração de casa com painéis solares no telhado, sol, inversor, medidor bidirecional e técnico sobre gramado"></div>

    <div class="footer-line"></div>
    <div class="footer-band"></div>
  </section>
</body>
</html>
```